Lumo Bathrooms Facelift. Moving the business in to the next professional level.

I'm currently revamping my bathroom renovation business. Part of this revamp includes our marketing strategy to better position ourselves as a professional business. As the name suggests, we primarily do bathroom renovations of all shapes, sizes and budgets. I'd like a business card design that is simple, yet displays our company as sophisticated.
What I'd like is to have a card that incorporates the following elements;
- Orange set as the primary colour and Charcoal/Grey as a complement colour. The card can also include white and/or black.
- I'd like a hexagon pattern within the charcoal/grey (In gloss perhaps to break it up a bit)
- I only want the Lumo Bathrooms logo on the front of the card
- Back of the card would include contact details
- The bottom edges of the card would be rounded off
- I've attached the company name. I'd like to keep lumo as it is. Bathrooms can be modified
Industry/Entity Type
Marketing

```html
<!DOCTYPE html>
<html lang="en">
<head>
<meta charset="utf-8">
<title>Lumo Bathrooms – Business Card</title>
<link href="https://fonts.googleapis.com/css2?family=Questrial&display=swap" rel="stylesheet">
<style>
  :root {
    --backdrop: #e6e2dc;
    --charcoal: #2f3032;
    --charcoal-light: #3a3b3e;
    --charcoal-dark: #26272a;
    --orange: #ef7b22;
    --silver: #b9b9b9;
    --text-light: #c9c9c9;
  }
  * { margin: 0; padding: 0; box-sizing: border-box; }
  html, body { width: 1200px; height: 1000px; overflow: hidden; }
  body {
    background: var(--backdrop);
    font-family: "Questrial", "Century Gothic", sans-serif;
    position: relative;
  }
  .card {
    position: absolute;
    left: 267px;
    width: 665px;
    height: 398px;
    border-radius: 24px;
    overflow: hidden;
    background: var(--charcoal);
    box-shadow: 0 6px 16px rgba(0,0,0,0.25);
  }
  .card--front { top: 73px; }
  .card--back { top: 532px; }
  .facet-pattern {
    position: absolute;
    inset: 0;
    background: linear-gradient(135deg, var(--charcoal-light) 0%, var(--charcoal) 45%, var(--charcoal-dark) 100%);
  }
  .frame {
    position: absolute;
    left: 23px; top: 22px;
    width: 617px; height: 354px;
    border: 2.5px solid var(--orange);
    border-radius: 18px;
  }
  .wordmark { position: absolute; color: var(--silver); line-height: 1; }
  .wordmark__name { display: block; font-size: 96px; letter-spacing: 4px; }
  .wordmark__sub { display: block; font-size: 26px; letter-spacing: 1.5px; text-align: right; }
  .card--front .wordmark { left: 163px; top: 132px; width: 330px; }
  .card--back .wordmark { left: 33px; top: 54px; width: 282px; }
  .card--back .wordmark__name { font-size: 82px; }
  .card--back .wordmark__sub { font-size: 23px; margin-top: 2px; }

  .contact { position: absolute; left: 381px; top: 182px; right: 0; color: var(--text-light); }
  .contact__name { font-size: 24px; line-height: 1; }
  .contact__role { font-size: 16px; margin-top: 4px; }
  .contact__rule { height: 2px; background: var(--orange); margin: 10px 0 8px; }
  .contact__address { font-size: 16.5px; line-height: 20px; }
  .contact__list { list-style: none; margin-top: 12px; font-size: 16.5px; line-height: 21px; }
  .contact__list li { display: flex; align-items: center; gap: 7px; }
  .contact__list svg { width: 13px; height: 13px; fill: var(--orange); flex: none; }
  .accent { color: var(--orange); }
</style>
</head>
<body>
  <section class="card card--front" aria-label="Card front">
    <div class="facet-pattern" role="img" aria-label="Faint dark geometric facet pattern"></div>
    <div class="frame"></div>
    <div class="wordmark">
      <span class="wordmark__name">lumo</span>
      <span class="wordmark__sub">BATHROOMS</span>
    </div>
  </section>

  <section class="card card--back" aria-label="Card back">
    <div class="facet-pattern" role="img" aria-label="Faint dark geometric facet pattern"></div>
    <div class="wordmark">
      <span class="wordmark__name">lumo</span>
      <span class="wordmark__sub">BATHROOMS</span>
    </div>
    <div class="contact">
      <p class="contact__name">Sam Carter</p>
      <p class="contact__role">Founder</p>
      <div class="contact__rule"></div>
      <p class="contact__address">218 Wattle Grove Road 12th,<br>Kelvale, VIC 3861</p>
      <div class="contact__rule" style="margin-bottom:0"></div>
      <ul class="contact__list">
        <li><svg viewBox="0 0 16 16" aria-hidden="true"><path d="M3 1l3 3-2 2c1 2 3 4 5 5l2-2 3 3-2 2C7 14 2 9 1 3z"/></svg>+ 555 014 2783</li>
        <li><svg viewBox="0 0 16 16" aria-hidden="true"><path d="M1 3h14v10H1z M1 3l7 6 7-6" stroke="#2f3032" stroke-width="1"/></svg>info@lumobathroom.com</li>
        <li><svg viewBox="0 0 16 16" aria-hidden="true"><circle cx="8" cy="8" r="7"/><path d="M1 8h14M8 1c3 3 3 11 0 14M8 1c-3 3-3 11 0 14" stroke="#2f3032" stroke-width="1" fill="none"/></svg>www.<span class="accent">lumobathroom</span>.com</li>
      </ul>
    </div>
  </section>
</body>
</html>
```